Bluestone Freight

We are a 3PL freight brokerage company looking to create a website to attract new customers. Some ideas on how other freight websites look is located at these links, https://www.marigoldhaulerline.com/services, https://quillmarkcargo.com/freight-brokerage/.
We would like to have a quote feature implemented into this website.

We specialize in heavy-haul, specialized loads, flatbed, and dry vans.

```html
<!DOCTYPE html>
<html lang="en">
<head>
<meta charset="utf-8">
<title>Bluestone Freight – Transportation and Logistics Solutions</title>
<link href="https://fonts.googleapis.com/css2?family=Montserrat:wght@400;500;600;700;800&display=swap" rel="stylesheet">
<style>
:root{
  --navy:#1c3b6c;
  --navy-deep:#12284d;
  --gold:#b8952f;
  --ink:#1b1b1b;
  --muted:#5b5b5b;
  --soft:#f4f4f4;
  --footer:#2c2c2c;
  --white:#ffffff;
}
*{margin:0;padding:0;box-sizing:border-box}
html,body{width:1200px;height:3745px;overflow:hidden}
body{font-family:"Montserrat",sans-serif;color:var(--ink);background:var(--white);position:relative}
.abs{position:absolute}
.btn{position:absolute;background:var(--gold);color:var(--white);font-weight:700;font-size:15px;display:flex;align-items:center;justify-content:center;gap:8px}
.chev{font-weight:800}
.eyebrow{position:absolute;color:var(--gold);font-size:14px;letter-spacing:.5px;display:flex;align-items:center;gap:10px}
.eyebrow .dash{display:inline-block;width:40px;height:6px;border-top:1.5px solid var(--navy);border-bottom:1.5px solid var(--navy)}
.h2{position:absolute;font-size:32px;font-weight:400;line-height:41px}
.h2 b{font-weight:800}
.para{position:absolute;font-size:15px;line-height:22.5px;color:var(--muted)}

/* top bar & header */
.topbar{left:0;top:0;width:1200px;height:22px;background:var(--navy)}
.topbar .info{position:absolute;top:4px;font-size:11px;color:#d7dce6;display:flex;align-items:center;gap:5px}
.header{left:0;top:22px;width:1200px;height:77px;background:var(--white);box-shadow:0 1px 0 #eee}
.logo-box{left:116px;top:0;width:175px;height:99px;background:var(--white);display:flex;flex-direction:column;align-items:center;justify-content:center;gap:2px;color:var(--navy);font-weight:800}
.logo-box .l1{font-size:20px;letter-spacing:.5px}
.logo-box .l2{font-size:13px;letter-spacing:3px}
.nav a{position:absolute;top:52px;font-size:15px;color:var(--ink);text-decoration:none}
.nav a.active{color:var(--gold)}

/* hero */
.hero{left:0;top:99px;width:1200px;height:560px;background:linear-gradient(180deg,#6f6e72 0%,#b58a62 30%,#4b4d55 65%,#2a2b30 100%)}
.hero-title{left:125px;top:278px;color:var(--white);font-size:44px;line-height:56px;font-weight:400;letter-spacing:1px}
.hero-title b{font-weight:800}
.hero-sub{left:126px;top:403px;color:var(--white);font-size:16px;font-weight:700}

/* about */
.about-img{left:125px;top:753px;width:461px;height:428px;background:linear-gradient(135deg,#b7bcc4,#6e8fb3 45%,#4c6f98 70%,#2f4056)}
.link-more{position:absolute;color:var(--gold);font-weight:700;font-size:15px}

/* stats */
.stats{left:0;top:1278px;width:1200px;height:268px;background:linear-gradient(90deg,var(--navy-deep),var(--navy) 50%,var(--navy-deep))}
.stat{position:absolute;top:72px;width:220px;text-align:center;color:var(--white)}
.stat .num{font-size:32px;font-weight:700;margin-top:10px}
.stat .lbl{font-size:15px;margin-top:2px}
.divider{position:absolute;top:50px;width:1px;height:150px;background:rgba(255,255,255,.35)}

/* services */
.services{left:0;top:1546px;width:1200px;height:614px;background:var(--soft)}
.card{position:absolute;top:1744px;width:218px;height:313px;background:var(--white);border:1px solid #e6e6e6;text-align:center}
.card .ph{height:188px}
.card h3{font-size:13px;font-weight:700;color:var(--navy);margin-top:11px;letter-spacing:.4px}
.card p{font-size:11.5px;line-height:17.5px;color:#8a8a8a;margin:8px 14px 0}
.card .lm{font-size:12px;color:var(--gold);margin-top:8px}

/* carriers */
.carriers{left:0;top:2160px;width:1200px;height:548px;background:linear-gradient(90deg,#f2f3f5,#e4e6ea 60%,#eceef1)}
.frame{left:576px;top:2278px;width:497px;height:332px;background:var(--white);padding:7px}
.frame .ph{width:100%;height:100%;background:linear-gradient(90deg,#a88d6f,#c9b79d 40%,#6c7b86 70%,#cfd6de);display:flex;flex-direction:column;align-items:flex-start;justify-content:center;padding-left:52px;color:var(--white);font-weight:800}

/* partners */
.partner{position:absolute;top:2764px;font-size:28px;font-weight:700;color:#a8a8a8}

/* quote */
.quote{left:0;top:2855px;width:1200px;height:565px;background:linear-gradient(90deg,#3a4f6c 0%,#2f4a75 35%,var(--navy) 55%,var(--navy-deep) 100%)}
.field{position:absolute;border-bottom:1px solid rgba(255,255,255,.5);color:#d5dbe6;font-size:12px;display:flex;align-items:center;gap:8px;padding-bottom:6px}

/* footer */
.footer{left:0;top:3404px;width:1200px;height:341px;background:var(--footer)}
.fcol h4{position:absolute;top:3464px;color:var(--white);font-size:14px;font-weight:700;letter-spacing:.5px}
.fcol a{position:absolute;color:#e2e2e2;font-size:14px;text-decoration:none}
.finfo{position:absolute;color:#e2e2e2;font-size:14px;line-height:18px;display:flex;gap:7px}
.social{position:absolute;top:3589px;width:28px;height:28px;border-radius:50%;background:#d9d9d9}
.copy{position:absolute;top:3709px;font-size:12px;color:#d0d0d0}
</style>
</head>
<body>

<!-- top bar -->
<div class="abs topbar">
  <div class="info" style="left:690px">
    <svg width="10" height="12" viewBox="0 0 10 12"><path d="M5 0C2.2 0 0 2.2 0 4.8 0 8.4 5 12 5 12s5-3.6 5-7.2C10 2.2 7.8 0 5 0zm0 6.8A2 2 0 1 1 5 2.8a2 2 0 0 1 0 4z" fill="#b8952f"/></svg>
    418 Harbor Line Rd. Dayton, Ohio 45402 <span style="margin:0 8px">|</span>
    <svg width="11" height="11" viewBox="0 0 24 24"><path d="M6.6 10.8a15 15 0 0 0 6.6 6.6l2.2-2.2c.3-.3.7-.4 1-.2 1.1.4 2.3.6 3.6.6.6 0 1 .4 1 1V20c0 .6-.4 1-1 1A17 17 0 0 1 3 4c0-.6.4-1 1-1h3.5c.6 0 1 .4 1 1 0 1.3.2 2.5.6 3.6.1.3 0 .7-.2 1l-2.3 2.2z" fill="#b8952f"/></svg>
    (614) 555-0187
  </div>
</div>

<!-- header -->
<div class="abs header"></div>
<div class="abs logo-box"><span class="l1">BLUESTONE</span><span class="l2">FREIGHT</span></div>
<nav class="nav">
  <a class="active" style="left:553px">Home</a>
  <a style="left:635px">About Us</a>
  <a style="left:740px">Services</a>
  <a style="left:842px">Carriers</a>
</nav>
<div class="btn" style="left:931px;top:39px;width:142px;height:44px;font-weight:500">Contact Us <span class="chev">›</span></div>

<!-- hero -->
<div class="abs hero" role="img" aria-label="Branded semi truck driving on a highway at sunset"></div>
<h1 class="abs hero-title">TRANSPORTATION AND<br>LOGISTICS <b>SOLUTIONS</b></h1>
<div class="abs hero-sub">3PL Freight Brokerage Company</div>
<div class="btn" style="left:125px;top:455px;width:151px;height:45px">Get A Quote <span class="chev">›</span></div>
<svg class="abs" style="left:0;top:560px" width="1200" height="110" viewBox="0 0 1200 110">
  <polygon points="0,90 1200,25 1200,110 0,110" fill="#fff"/>
  <polygon points="0,88 1085,32 1085,61 0,96" fill="#b8952f"/>
</svg>

<!-- about -->
<div class="abs about-img" role="img" aria-label="Two warehouse workers checking a parcel against a tablet"></div>
<div class="eyebrow" style="left:668px;top:772px">ABOUT US <span class="dash"></span></div>
<h2 class="h2" style="left:668px;top:797px">We Provide <b>High Quality</b><br>Logistics Services</h2>
<p class="para" style="left:668px;top:900px;width:380px">Lorem ipsum dolor sit amet, consectetur adipiscing elit. Morbi turpis tortor malesuada ultrices vehicula id nulla eu. Vehicula volutpat morbi dolor neque egestas quis. Quam et tincidunt neque at. Neque augue lectus sit.</p>
<p class="para" style="left:668px;top:1027px;width:380px">Elementum sodales feugiat facilisi nulla. Ultricies tortor, fames nunc quisque dui. Duis cursus tristique sem in sit scelerisque amet varius tellus.</p>
<div class="link-more" style="left:668px;top:1131px">More About Us &nbsp;<span class="chev">›</span></div>

<!-- stats -->
<div class="abs stats">
  <div class="stat" style="left:134px">
    <svg width="40" height="56" viewBox="0 0 40 56"><circle cx="20" cy="8" r="7" fill="#b8952f"/><path d="M8 20h24l-4 14H12z" fill="#b8952f"/><polygon points="20,30 24,40 34,40 26,46 29,56 20,50 11,56 14,46 6,40 16,40" fill="#b8952f"/></svg>
    <div class="num">10+</div><div class="lbl">Years of experience</div>
  </div>
  <div class="divider" style="left:362px"></div>
  <div class="stat" style="left:371px">
    <svg width="60" height="56" viewBox="0 0 60 56"><path d="M2 16l12-6 10 4 8-4 14 2 12 6-6 12-8 8-6 4-6-4-10-6-10-8z" fill="#b8952f"/><path d="M22 24l8 6 8-6" stroke="#1c3b6c" stroke-width="2" fill="none"/></svg>
    <div class="num">500+</div><div class="lbl">Satisfied clients</div>
  </div>
  <div class="divider" style="left:599px"></div>
  <div class="stat" style="left:608px">
    <svg width="40" height="56" viewBox="0 0 40 56"><rect x="4" y="6" width="32" height="38" rx="4" fill="#b8952f"/><rect x="9" y="11" width="22" height="12" fill="#1c3b6c"/><circle cx="11" cy="34" r="3" fill="#1c3b6c"/><circle cx="29" cy="34" r="3" fill="#1c3b6c"/><rect x="6" y="44" width="7" height="8" fill="#b8952f"/><rect x="27" y="44" width="7" height="8" fill="#b8952f"/></svg>
    <div class="num">1200+</div><div class="lbl">Road trucking</div>
  </div>
  <div class="divider" style="left:836px"></div>
  <div class="stat" style="left:845px">
    <svg width="44" height="56" viewBox="0 0 44 56"><circle cx="14" cy="7" r="6" fill="#b8952f"/><path d="M8 16h10l4 16h14v6H18z" fill="#b8952f"/><path d="M6 18v24h20l4 14" stroke="#b8952f" stroke-width="3" fill="none"/></svg>
    <div class="num">100+</div><div class="lbl">Workers in team</div>
  </div>
</div>

<!-- services -->
<div class="abs services"></div>
<div class="eyebrow" style="left:492px;top:1643px"><span class="dash"></span> OUR SERVICES <span class="dash"></span></div>
<h2 class="h2" style="left:0;width:1200px;text-align:center;top:1667px">Featured <b>Services</b></h2>

<div class="card" style="left:126px"><div class="ph" role="img" aria-label="Heavy tank load on a multi-axle trailer" style="background:linear-gradient(180deg,#8da3bd,#6c7480 55%,#3e3f44)"></div><h3>HEAVY-HAUL</h3><p>Lorem ipsum dolor sit amet, consectetur adipiscing elit morbi turpis tortor malesuada.</p><div class="lm">Learn More ›</div></div>
<div class="card" style="left:369px"><div class="ph" role="img" aria-label="Oversized wrapped cargo on a low trailer" style="background:linear-gradient(180deg,#7f8b98,#c9cdd3 45%,#8a7a3e 80%,#4a4a4a)"></div><h3>SPECIALIZED LOADS</h3><p>Lorem ipsum dolor sit amet, consectetur adipiscing elit morbi turpis tortor malesuada.</p><div class="lm">Learn More ›</div></div>
<div class="card" style="left:612px"><div class="ph" role="img" aria-label="White flatbed truck parked in a row" style="background:linear-gradient(180deg,#5f8ac4,#e8ecef 45%,#b5bcc2 80%,#6a6e72)"></div><h3>FLATBED VANS</h3><p>Lorem ipsum dolor sit amet, consectetur adipiscing elit morbi turpis tortor malesuada.</p><div class="lm">Learn More ›</div></div>
<div class="card" style="left:855px"><div class="ph" role="img" aria-label="Red semi truck hauling a dry van trailer" style="background:linear-gradient(180deg,#9fb0b5,#b93a3a 55%,#5d6064)"></div><h3>DRY VANS</h3><p>Lorem ipsum dolor sit amet, consectetur adipiscing elit morbi turpis tortor malesuada.</p><div class="lm">Learn More ›</div></div>

<!-- carriers -->
<div class="abs carriers" role="img" aria-label="Faded warehouse shelving background"></div>
<div class="eyebrow" style="left:126px;top:2284px">CARRIERS <span class="dash"></span></div>
<h2 class="h2" style="left:126px;top:2304px">More Than Just A<br><b>Delivery</b></h2>
<p class="para" style="left:126px;top:2408px;width:415px">Vehicula volutpat morbi dolor neque egestas quis. Quam et tincidunt neque at. Neque augue lectus sit.</p>
<p class="para" style="left:126px;top:2466px;width:415px">Elementum sodales feugiat facilisi nulla. Ultricies tortor, fames nunc quisque dui. Duis cursus tristique sem in sit scelerisque amet varius tellus.</p>
<div class="btn" style="left:126px;top:2564px;width:155px;height:46px">Apply Today <span class="chev">›</span></div>
<div class="abs frame"><div class="ph" role="img" aria-label="Smiling warehouse worker holding a clipboard"><span style="font-size:26px;letter-spacing:.5px">BLUESTONE</span><span style="font-size:17px;letter-spacing:4px">FREIGHT</span></div></div>

<!-- partners -->
<div class="partner" style="left:134px">Northfield</div>
<div class="partner" style="left:378px;font-size:22px">Kestrel Lines</div>
<div class="partner" style="left:562px;font-size:26px">Larkspur</div>
<div class="partner" style="left:782px;font-size:24px">Oakmere</div>
<div class="partner" style="left:966px;font-size:28px">Tidewell</div>

<!-- quote -->
<div class="abs quote"></div>
<div class="abs" role="img" aria-label="Truck driving along a road at dusk" style="left:0;top:2855px;width:600px;height:565px;background:linear-gradient(90deg,rgba(140,120,90,.55),rgba(60,85,120,.4) 60%,rgba(28,59,108,0))"></div>
<h2 class="h2" style="left:676px;top:2940px;color:#fff">Get A <b>Quote</b></h2>
<p class="abs" style="left:620px;top:2998px;width:400px;color:#fff;font-size:13px;font-weight:600;line-height:20px">We will be happy to keep in touch with you and to answer any questions.</p>
<div class="abs" style="left:620px;top:3066px;font-size:10px;color:#c9d0dc">Name</div>
<div class="field" style="left:620px;top:3086px;width:186px;color:#fff;font-weight:700;justify-content:space-between">Jordan Avery
  <svg width="12" height="12" viewBox="0 0 12 12"><circle cx="6" cy="3.5" r="2.5" stroke="#fff" fill="none"/><path d="M1 11c0-3 2.5-4.5 5-4.5s5 1.5 5 4.5" stroke="#fff" fill="none"/></svg></div>
<div class="field" style="left:862px;top:3086px;width:188px">
  <svg width="12" height="12" viewBox="0 0 24 24"><path d="M6.6 10.8a15 15 0 0 0 6.6 6.6l2.2-2.2c.3-.3.7-.4 1-.2 1.1.4 2.3.6 3.6.6.6 0 1 .4 1 1V20c0 .6-.4 1-1 1A17 17 0 0 1 3 4c0-.6.4-1 1-1h3.5c.6 0 1 .4 1 1 0 1.3.2 2.5.6 3.6.1.3 0 .7-.2 1l-2.3 2.2z" stroke="#d5dbe6" stroke-width="2" fill="none"/></svg>Phone</div>
<div class="field" style="left:620px;top:3150px;width:430px">
  <svg width="13" height="10" viewBox="0 0 13 10"><rect x=".5" y=".5" width="12" height="9" stroke="#d5dbe6" fill="none"/><path d="M.5.5l6 5 6-5" stroke="#d5dbe6" fill="none"/></svg>E-mail</div>
<div class="field" style="left:620px;top:3214px;width:430px">
  <svg width="13" height="12" viewBox="0 0 13 12"><path d="M.5.5h12v8h-8l-3 3v-3h-1z" stroke="#d5dbe6" fill="none"/></svg>Message</div>
<div class="btn" style="left:620px;top:3271px;width:150px;height:45px">Get A Quote <span class="chev">›</span></div>

<!-- footer -->
<svg class="abs" style="left:0;top:3350px" width="1200" height="70" viewBox="0 0 1200 70">
  <polygon points="164,13 1200,50 1200,70 0,70 0,54" fill="#2c2c2c"/>
  <polygon points="164,13 1200,44 1200,50 164,20" fill="#b8952f"/>
</svg>
<div class="abs footer"></div>
<div class="abs" style="left:1056px;top:3380px;width:54px;height:54px;border-radius:50%;background:#fff;display:flex;align-items:center;justify-content:center">
  <svg width="14" height="9" viewBox="0 0 14 9"><path d="M1 8l6-6 6 6" stroke="#b8952f" stroke-width="2.2" fill="none"/></svg>
</div>
<div class="abs" style="left:116px;top:3520px;width:225px;text-align:center;color:#fff;font-weight:800;line-height:1.1">
  <div style="font-size:27px;letter-spacing:1px">BLUESTONE</div><div style="font-size:17px;letter-spacing:5px">FREIGHT</div>
</div>
<div class="social" style="left:156px"></div>
<div class="social" style="left:190px"></div>
<div class="social" style="left:225px"></div>
<div class="social" style="left:259px"></div>

<div class="fcol">
  <h4 style="left:468px">QUICK LINKS</h4>
  <a style="left:468px;top:3508px">Home</a>
  <a style="left:468px;top:3538px">About Us</a>
  <a style="left:468px;top:3567px">Services</a>
  <a style="left:468px;top:3598px">Carriers</a>
  <a style="left:468px;top:3628px">Contact Us</a>
  <h4 style="left:659px">OUR SERVICES</h4>
  <a style="left:659px;top:3508px">Heavy-Haul</a>
  <a style="left:659px;top:3538px">Specialized Loads</a>
  <a style="left:659px;top:3567px">Flatbed Vans</a>
  <a style="left:659px;top:3598px">Dry Vans</a>
  <h4 style="left:867px">GET IN TOUCH</h4>
</div>
<div class="finfo" style="left:867px;top:3506px;width:220px">
  <svg width="10" height="12" viewBox="0 0 10 12" style="flex:none;margin-top:3px"><path d="M5 0C2.2 0 0 2.2 0 4.8 0 8.4 5 12 5 12s5-3.6 5-7.2C10 2.2 7.8 0 5 0zm0 6.8A2 2 0 1 1 5 2.8a2 2 0 0 1 0 4z" fill="#b8952f"/></svg>
  <span>418 Harbor Line Rd. Dayton, Ohio 45402</span></div>
<div class="finfo" style="left:867px;top:3562px">
  <svg width="11" height="11" viewBox="0 0 24 24" style="margin-top:4px"><path d="M6.6 10.8a15 15 0 0 0 6.6 6.6l2.2-2.2c.3-.3.7-.4 1-.2 1.1.4 2.3.6 3.6.6.6 0 1 .4 1 1V20c0 .6-.4 1-1 1A17 17 0 0 1 3 4c0-.6.4-1 1-1h3.5c.6 0 1 .4 1 1 0 1.3.2 2.5.6 3.6.1.3 0 .7-.2 1l-2.3 2.2z" fill="#b8952f"/></svg>(614) 555-0187</div>
<div class="finfo" style="left:867px;top:3598px">
  <svg width="12" height="9" viewBox="0 0 12 9" style="margin-top:5px"><rect width="12" height="9" fill="#b8952f"/><path d="M0 0l6 5 6-5" stroke="#2c2c2c" fill="none"/></svg>hello@bluestonefreight.example</div>

<div class="abs" style="left:120px;top:3679px;width:952px;height:1px;background:#555"></div>
<div class="copy" style="left:120px">©Copyright 2022. <u>BLUESTONE FREIGHT</u> | All Rights Reserved</div>
<div class="copy" style="left:840px">Privacy Policy &nbsp;| &nbsp;Terms and Conditions</div>

</body>
</html>
```